Clean Plinth Ads Banner Design For A Finance Company

Hi,
We're a UK based finance company and are looking for new banner ads to use on the Plinth Display Network.
We want the end product to stand out by using strong, minimal design - ideally starting from a dark theme, although I'm open to ideas.
The copy should read:
'Fast Bridging Loans From 0.39% PM'
Once we have these designs agreed, we are looking to replicate them for other products, changing only the text on each ad - for example, 'commercial mortgage service you can rely on' or 'development finance service you can rely on'.
The colours used on our website are the following:
Black - #040303
Orange - #f79124
White - #ffffff
Grey - #ffffff
Example ads that I like - https://www.brimcastle.com/wp-content/uploads/2021/07/plinth-display-ads-example-2-final.png.webp
2 - https://quendrahub.com/wp-content/uploads/2020/03/fbdd56ba3bd16c7a8debb13a411de786.jpg

```html
<!DOCTYPE html>
<html lang="en">
<head>
<meta charset="UTF-8">
<title>Orvane Finance – Bridging Loan Banner</title>
<link href="https://fonts.googleapis.com/css2?family=Open+Sans:wght@400;600;700;800&display=swap" rel="stylesheet">
<style>
  :root {
    --brand-black: #1d1b1b;
    --panel-black: #242121;
    --brand-orange: #f79124;
    --brand-white: #ffffff;
    --photo-dark: #2e2824;
    --photo-mid: #5a4a3e;
    --photo-light: #8a7462;
  }
  * { margin: 0; padding: 0; box-sizing: border-box; }
  html, body {
    width: 1200px;
    height: 148px;
    overflow: hidden;
    background: var(--brand-black);
    font-family: "Open Sans", Arial, sans-serif;
  }
  .banner {
    position: relative;
    width: 1200px;
    height: 148px;
    background: var(--brand-black);
    overflow: hidden;
  }
  .banner-shapes {
    position: absolute;
    inset: 0;
  }
  .brand-name {
    position: absolute;
    left: 22px;
    top: 28px;
    width: 230px;
    color: var(--brand-orange);
    font-weight: 700;
    text-align: center;
    line-height: 1;
  }
  .brand-name .brand-word {
    display: block;
    font-size: 58px;
    letter-spacing: -1px;
  }
  .brand-name .brand-sub {
    display: block;
    font-size: 17px;
    margin-top: 8px;
  }
  .headline {
    position: absolute;
    left: 310px;
    width: 420px;
    top: 26px;
    text-align: center;
    color: var(--brand-white);
    font-size: 33px;
    line-height: 44px;
    font-weight: 400;
    white-space: nowrap;
  }
  .headline .highlight {
    color: var(--brand-orange);
    font-weight: 700;
  }
  .selling-points {
    position: absolute;
    left: 800px;
    width: 200px;
    top: 18px;
    text-align: center;
    color: var(--brand-white);
    font-size: 24px;
    line-height: 37px;
    font-weight: 400;
    white-space: nowrap;
  }
  .selling-points .accent {
    color: var(--brand-orange);
    font-weight: 700;
  }
  .cta-button {
    position: absolute;
    left: 1008px;
    top: 53px;
    width: 120px;
    height: 42px;
    border-radius: 21px;
    background: var(--brand-orange);
    color: var(--brand-black);
    font-size: 13px;
    font-weight: 700;
    letter-spacing: 0.5px;
    display: flex;
    align-items: center;
    justify-content: center;
    text-decoration: none;
  }
</style>
</head>
<body>
  <div class="banner">
    <svg class="banner-shapes" width="1200" height="148" viewBox="0 0 1200 148">
      <defs>
        <linearGradient id="photoTone" x1="0" y1="0" x2="1" y2="1">
          <stop offset="0" stop-color="#8a7462"/>
          <stop offset="0.45" stop-color="#5a4a3e"/>
          <stop offset="1" stop-color="#2e2824"/>
        </linearGradient>
      </defs>
      <g role="img" aria-label="Photo of a small model house with a set of keys on a wooden desk">
        <path d="M300,0 Q262,74 300,148 L830,148 Q790,74 830,0 Z" fill="url(#photoTone)"/>
        <path d="M300,0 Q262,74 300,148 L830,148 Q790,74 830,0 Z" fill="#000" opacity="0.35"/>
      </g>
      <path d="M300,0 Q262,74 300,148" fill="none" stroke="#f79124" stroke-width="7"/>
      <path d="M830,0 Q790,74 830,148 L1200,148 L1200,0 Z" fill="#242121"/>
    </svg>

    <div class="brand-name">
      <span class="brand-word">Orvane</span>
      <span class="brand-sub">Finance Limited</span>
    </div>

    <h1 class="headline">
      <span class="highlight">Bridging</span> Loan Service<br>You Can Rely On
    </h1>

    <p class="selling-points">
      <span class="accent">5★ Rated</span><br>
      <span class="accent">Service</span> &amp;<br>
      No Broker Fees
    </p>

    <a class="cta-button" href="#">LEARN MORE</a>
  </div>
</body>
</html>
```